Meadowlark Behavioral Partners, LLC Needs Modern Business Card Design.

We provide behavioral health services from western Kansas to eastern Kansas. There is an abundance of competition for the services we provide with our main competitor being larger and having significantly more financial resources; however, the quality of services we provide is greater and we have started to catch the attention of the State of Kansas. We had a great logo designed by PixelGuild - this will be used to build upon our brand. The logo (attached) should be used in the card development. We want something unique, modern, but also a card design that clearly states our name, contact info, provides the name and unqiue location of each clinician, etc. Rounded edges, or a unique size, just something that makes our business card stand out from others. I have also uploaded each clinician's name and their unique location and phone number.

Our idea is to have one side be black with our logo. Then, on the other side have business cards for each individual. Plus, we want one card that is "generic" with no specific clinician's name listed so that we can give clients an appointment card when they leave. Some clinicians have two locations - we're open to design and background color, but we have started going with branding colors of black, the yellow in the logo files attached, and sometimes a gray. Our new office has been decorated using this theme.

Target Market(s)

individuals and families in need of behavioral health services; potential professional referral sources; existing referral sources

Industry/Entity Type

Business

Contact Information for Business Card

I attached a Word doc that provides clinician names, credentials and location information specific to each individual.

Font styles to use
Serif

Colors
000000
fbed22
dbdbdb
9d9d9d
c3c3c3

Requirements
Must have
• 1) use of the company logo that has been attached; 2) a template that provides us space to individualize business cards for all of our clinicians; 3) should stick to the colors we are branding with: black, yellow from the logo file, maybe a gray shade and we're open to a suggestion on a shade of white.
Nice to have
• Group discussion culminated in the thought that one side would be black with just our logo - no clinician names, etc. A unique design - rounded edges, unique size, some catchy lay-out would be nice.
Should not have
• Must not be too busy. Should look "clean." The project should stick to branding colors: black, yellow (from the logo file), maybe a gray and shade of white.

```html
<!DOCTYPE html>
<html lang="en">
<head>
<meta charset="utf-8">
<title>Meadowlark Behavioral Partners – Business Card</title>
<link rel="stylesheet" href="https://fonts.googleapis.com/css2?family=Cinzel:wght@600&family=PT+Sans:wght@400;700&display=swap">
<style>
  :root {
    --black: #000000;
    --card-black: #0a0a0a;
    --yellow: #fbed22;
    --gold: #f4c21a;
    --orange: #f6a91f;
    --gray-light: #e2e2e2;
    --gray-mid: #c3c3c3;
    --gray-dark: #9d9d9d;
    --backdrop: #2b2d31;
    --ink: #1a1a1a;
    --white: #ffffff;
  }
  * { box-sizing: border-box; margin: 0; padding: 0; }
  html, body { width: 1200px; height: 1000px; overflow: hidden; }
  body {
    background: var(--backdrop);
    position: relative;
    font-family: "PT Sans", sans-serif;
  }
  .card {
    position: absolute;
    left: 250px;
    width: 700px;
    height: 400px;
    border-radius: 40px;
    overflow: hidden;
  }
  .card--front { top: 70px; background: var(--card-black); }
  .card--back  { top: 530px; background: var(--gray-light); }

  .front-brand {
    position: absolute;
    inset: 0;
    display: flex;
    align-items: center;
    justify-content: center;
    gap: 18px;
  }
  .front-brand__dot {
    width: 34px; height: 34px;
    border-radius: 50%;
    background: var(--gold);
  }
  .front-brand__name {
    font-family: "Cinzel", serif;
    font-weight: 600;
    color: var(--gold);
    font-size: 26px;
    letter-spacing: 1px;
    line-height: 1.25;
  }

  .band {
    position: absolute;
    left: 0; right: 0;
    top: 120px;
    height: 150px;
    display: flex;
  }
  .band__person {
    width: 300px;
    background: linear-gradient(90deg, var(--orange), var(--gold));
    border-right: 4px solid var(--white);
    display: flex;
    flex-direction: column;
    justify-content: flex-end;
    align-items: flex-end;
    padding: 0 22px 26px 0;
    color: var(--ink);
  }
  .person__name { font-weight: 700; font-size: 22px; }
  .person__title { font-weight: 700; font-size: 15px; }
  .band__contact {
    flex: 1;
    background: var(--yellow);
    padding: 10px 0 0 20px;
    font-size: 17px;
    line-height: 21px;
    color: var(--ink);
    list-style: none;
  }

  .back-mark {
    position: absolute;
    left: 300px;
    top: 300px;
    display: flex;
    align-items: center;
    gap: 10px;
  }
  .back-mark__dot {
    width: 30px; height: 30px;
    border-radius: 50%;
    background: var(--gray-mid);
  }
  .back-mark__name {
    font-family: "PT Sans", sans-serif;
    font-weight: 700;
    font-size: 14px;
    color: var(--gray-mid);
  }
</style>
</head>
<body>
  <section class="card card--front" aria-label="Card front">
    <div class="front-brand">
      <span class="front-brand__dot"></span>
      <p class="front-brand__name">Meadowlark<br>Behavioral Partners, LLC</p>
    </div>
  </section>

  <section class="card card--back" aria-label="Card back">
    <div class="band">
      <div class="band__person">
        <p class="person__name">Gordon T. Hale, LP</p>
        <p class="person__title">President</p>
      </div>
      <ul class="band__contact">
        <li>418 N. Larkin Ave.</li>
        <li>Wichita, Kansas 67214</li>
        <li>(316) 555-0142</li>
        <li>207 W. Elm St., Ste. 104</li>
        <li>Parsons, Kansas 67360</li>
        <li>(844) 555-0198</li>
      </ul>
    </div>
    <div class="back-mark">
      <span class="back-mark__dot"></span>
      <span class="back-mark__name">Meadowlark Behavioral Partners, LLC</span>
    </div>
  </section>
</body>
</html>
```